2 Page Business Flyer for Finance Business

Need a two page flyer created for a finance business. Lots of text and needs to fit on two pages.

Corporate business/banking look and feel. Not too many large images. Lots of white space, clean design. Attached is color palette and the text contents of the flyer.

```html
<!DOCTYPE html>
<html lang="en">
<head>
<meta charset="utf-8">
<title>Vanilla Option Flyer</title>
<link rel="stylesheet" href="https://fonts.googleapis.com/css2?family=Arimo:wght@400;700&display=swap">
<style>
  :root {
    --backdrop: #2a2e38;
    --paper: #ffffff;
    --red: #c8473f;
    --navy: #1d215e;
    --lavender: #6f6d95;
    --ink: #4a4d57;
    --ink-dark: #1d215e;
    --tech-deep: #06152e;
    --tech-glow: #1f7fd0;
    --office-light: #dfe4ea;
    --office-mid: #8a939f;
  }
  * { box-sizing: border-box; margin: 0; padding: 0; }
  html, body { width: 1200px; height: 950px; overflow: hidden; }
  body {
    background: var(--backdrop);
    font-family: "Arimo", Arial, sans-serif;
    color: var(--ink);
    position: relative;
  }
  .page {
    position: absolute;
    top: 79px;
    width: 560px;
    height: 792px;
    background: var(--paper);
    overflow: hidden;
  }
  .page--front { left: 27px; }
  .page--back { left: 613px; }

  .block { position: absolute; }
  .square-red { background: var(--red); }
  .square-navy { background: var(--navy); }
  .square-lavender { background: var(--lavender); }

  .photo-tech {
    position: absolute; left: 0; top: 0; width: 500px; height: 320px;
    border-bottom-left-radius: 70px;
    background: radial-gradient(ellipse at 40% 45%, var(--tech-glow) 0%, #0b3f7a 35%, var(--tech-deep) 75%);
  }
  .photo-office {
    position: absolute; left: 30px; top: 40px; width: 220px; height: 170px;
    border-bottom-right-radius: 60px;
    background: linear-gradient(135deg, var(--office-light) 0%, var(--office-mid) 55%, #3b4456 100%);
  }
  .photo-chart {
    position: absolute; right: 0; top: 410px; width: 250px; height: 175px;
    border-top-left-radius: 60px;
    background: linear-gradient(135deg, #5f8fc6 0%, #1f4f93 50%, #0c2453 100%);
  }

  h1, h2 {
    font-weight: 700;
    color: var(--ink-dark);
    text-transform: uppercase;
    letter-spacing: 0.2px;
  }
  h1 { font-size: 17px; line-height: 1.15; }
  h2 { font-size: 15px; line-height: 1.15; }
  h3 {
    font-size: 8px; font-weight: 700; color: var(--red);
    text-transform: uppercase; margin: 10px 0 4px;
  }
  p, li { font-size: 7.4px; line-height: 1.45; }
  p + p { margin-top: 6px; }
  ul { list-style: none; margin: 6px 0; }
  li { position: relative; padding-left: 10px; margin-bottom: 2px; }
  li::before {
    content: ""; position: absolute; left: 1px; top: 3.5px;
    width: 3.5px; height: 3.5px; border-radius: 50%; background: var(--ink-dark);
  }
  .lead-in { color: var(--red); font-weight: 700; font-size: 8px; margin-top: 8px; }

  .front-title { position: absolute; left: 32px; top: 362px; width: 500px; }
  .front-body {
    position: absolute; left: 32px; top: 398px; width: 496px;
    display: grid; grid-template-columns: 1fr 1fr; column-gap: 20px;
  }

  .back-title { position: absolute; left: 272px; top: 62px; width: 250px; }
  .back-intro { position: absolute; left: 272px; top: 104px; width: 258px; }
  .back-left { position: absolute; left: 30px; top: 222px; width: 225px; }
  .back-left h2 { margin-top: 14px; margin-bottom: 6px; }
</style>
</head>
<body>

<section class="page page--front">
  <div class="photo-tech" role="img" aria-label="Photo of glowing blue digital data streams"></div>
  <div class="block square-red" style="left:300px;top:110px;width:260px;height:52px;"></div>
  <div class="block square-navy" style="left:300px;top:162px;width:220px;height:72px;"></div>
  <div class="block square-lavender" style="left:260px;top:234px;width:62px;height:62px;"></div>
  <div class="block square-red" style="left:258px;top:330px;width:18px;height:18px;"></div>

  <h1 class="front-title">How does a Vanilla Option contract work?</h1>

  <div class="front-body">
    <div class="col">
      <p>The buyer of a vanilla option receives protection against an adverse movement in the exchange rate while allowing full participation in a favourable move. At expiry the buyer of a Vanilla Option can choose to exercise the Option and take the currency, therefore providing flexibility in cases where the requirement to purchase foreign currency is not certain.</p>
      <p>A buyer of vanilla options is required to pay a premium (like an insurance premium) for the right, but not the obligation, to exchange currency at a predetermined rate on a predetermined date.</p>
      <ul>
        <li>Set a protection rate which will be your worst case scenario of expiry</li>
        <li>Determine the amount of currency you wish to protect</li>
        <li>Choose an expiry date for the contract</li>
        <li>Calculate the premium you are required to pay</li>
      </ul>
      <p class="lead-in">Let's look at an example: You are an importer.</p>
      <p>Your construction company has bid on a project that, if successful, will require you to import materials from the United States for use in construction. You have used today's pricing of materials in calculating your bid and want to protect against an adverse move in the US dollar exchange rate from eroding your margin if your bid is chosen for the project.</p>
    </div>
    <div class="col">
      <p>You choose to buy a Vanilla Call which will protect you from a rise in the USD/CAD exchange rate above your protection rate. You choose to buy protection on 500,000 USD with a protection rate (strike rate) of 1.3300 expiring in three months. You are required to pay a premium which in this case is calculated to be 1.6% or 11,200 CAD.</p>
      <p>Your bid is successful. If the exchange rate is below your protection rate at expiry, you have no obligation relating to the vanilla call and you are free to buy USD at the cheaper spot rate. If the exchange rate is above your protection rate, you have the right to purchase your USD at the protection rate, and thereby keep your original margin on the project.</p>
      <p>Your bid is not successful. You have no obligation relating to the vanilla option; however, if at expiry the exchange rate is above the protection rate, you may exercise your right to buy USD at the lower rate and simultaneously sell them at the higher spot rate, thereby recouping some or all of the premium paid to buy the option. Alternatively, if you find out your bid was not successful with time left until expiry, you may sell your option back into the market in the case that it still has residual value, which will depend on various market factors.</p>
    </div>
  </div>

  <div class="block square-navy" style="right:0;bottom:0;width:58px;height:58px;"></div>
  <div class="block square-red" style="right:58px;bottom:0;width:20px;height:20px;"></div>
</section>

<section class="page page--back">
  <div class="block square-navy" style="right:28px;top:0;width:40px;height:40px;"></div>
  <div class="block square-lavender" style="right:68px;top:30px;width:12px;height:12px;"></div>

  <div class="photo-office" role="img" aria-label="Photo of hands working on a laptop with a tablet"></div>

  <h2 class="back-title">What determines the price of a Vanilla Option?</h2>
  <div class="back-intro">
    <p>The cost of an option is determined by the premium that is required by the bank in order to offer the protection. The premium takes into account the following factors that are set by the client and the market, and determines how much the option is worth today.</p>
    <ul>
      <li>The current market Spot Rate</li>
      <li>Market volatility &ndash; the higher the volatility, the higher the premium</li>
      <li>The Term of the Option &ndash; a longer term typically increases cost</li>
      <li>The Strike Rate &ndash; the closer to spot, the higher the premium</li>
      <li>Interest rate differentials between the two currencies</li>
    </ul>
    <p>Volatility has a significant influence on pricing. When volatility is high the chance of the rate moving past the protection level rises, and the option becomes more valuable to hold and more costly to buy.</p>
  </div>

  <div class="back-left">
    <h3>Characteristics</h3>
    <ul>
      <li>You are looking for a straight forward hedging solution</li>
      <li>You want to retain full benefit from an appreciation of the currency you are exposed to</li>
      <li>The option provides protection on the whole of the exposure</li>
      <li>You are willing to pay the non-refundable premium</li>
    </ul>
    <h3>Advantages</h3>
    <ul>
      <li>You hedge your foreign currency exposure at a guaranteed rate</li>
      <li>You can choose the hedge rate that suits your budget</li>
      <li>Provides the ability to fully participate in a favourable exchange rate move</li>
      <li>You can choose to not exercise the option if it is not needed</li>
    </ul>
    <h3>Risks</h3>
    <ul>
      <li>Premium paid is non-refundable and remains your only obligation when buying vanilla options</li>
    </ul>
    <h2>Why use Vanilla Options?</h2>
    <p>Vanilla options are often compared to an insurance product. The buyer pays a premium for the right, but not the obligation, to exchange currency at the protection rate. Similar to insurance, the option can be set to expire unused if the market moves in your favour, while still guarding against an adverse move that would hurt your budget.</p>
  </div>

  <div class="photo-chart" role="img" aria-label="Photo of a glowing blue financial bar chart display"></div>
  <div class="block square-red" style="right:210px;top:555px;width:16px;height:16px;"></div>
  <div class="block square-navy" style="right:150px;top:560px;width:60px;height:60px;"></div>
  <div class="block square-red" style="right:0;top:600px;width:22px;height:22px;"></div>
</section>

</body>
</html>
```